Web Design - QM Field Outfitters

QM Field Outfitters is a future eCommerce wholesaler and retailer for tactical equipment such as: bulletproof vests, protective armor plates, ballistic helmets, military uniforms, magazines, military backpacks, etc. our main market will be the U.S market; U.S military, law enforcement and police. You can find the website on www.qmfieldout.com – I’m using a magento template but definitely need to customize the design. A clean and strong design is required and it also needs to incorporate eCommerce color scheme to highlight the important fields; BUY, SHOP, etc.

Please review the attached file to see our logo and incorporate the same style and colors

For exemple:
• http://www.738rangewear.com/
• http://www.plnwardworksco.com/
• http://www.vostaledger.com/
• http://www.brimwoldkit.com/
• http://www.mrvfld.com/
Thanks

Target Market(s)

U.S Military, U.S. Law Enforcement, Police

Industry/Entity Type

Shop

Requirements
Must have
• Home page must have a rotating / revolving banner with U.S Military / U.S Law Enforcement special forces / SWAT / QNU pictures in battlefield - at least 3-4 banners

```html
<!DOCTYPE html>
<html lang="en">
<head>
<meta charset="utf-8">
<title>QM Field Outfitters</title>
<link href="https://fonts.googleapis.com/css2?family=Open+Sans:wght@400;600;700&display=swap" rel="stylesheet">
<style>
:root{
  --orange:#e9a21f;
  --orange-dark:#c9810d;
  --page:#2b2b2b;
  --panel:#000;
  --card-border:#5b5b5b;
  --text:#cfcfcf;
  --white:#fff;
}
*{box-sizing:border-box;margin:0;padding:0}
html,body{width:1057px;height:1200px;overflow:hidden}
body{position:relative;font-family:"Open Sans",sans-serif;color:var(--text);
  background:radial-gradient(ellipse at 50% 40%,#3a3a3a 0%,#262626 70%,#1e1e1e 100%)}
.abs{position:absolute}
a{color:inherit;text-decoration:none}

/* top bar */
.search{left:106px;top:25px;width:216px;height:21px;background:#0c0c0c;border:1px solid #3a3a3a;font-size:8px;color:#777;padding:4px 6px}
.search svg{position:absolute;right:6px;top:5px}
.util{top:29px;left:548px;font-size:9.5px;color:#ddd;display:flex;gap:8px;align-items:center}
.util .sep{color:#aaa}
.login{left:890px;top:26px;width:53px;height:20px;background:var(--orange);border:1px solid #f3c15b;color:#fff;font-size:9px;font-weight:600;text-align:center;line-height:18px}

/* main panel */
.panel{left:106px;top:57px;width:845px;height:465px;background:var(--panel)}
.header-rule{left:106px;top:161px;width:845px;height:1px;background:#2a2a2a}
.brand{left:178px;top:97px;display:flex;align-items:center;gap:10px}
.brand-mark{width:44px;height:44px;border-radius:50%;background:var(--orange)}
.brand-name{font-size:17px;font-weight:700;color:var(--orange);letter-spacing:1px;text-transform:uppercase}
.nav{top:122px;left:536px;display:flex;gap:19px;font-size:12.5px;color:var(--orange)}
.nav .current{color:#fff;position:relative;padding:0 11px}
.nav .current::after{content:"";position:absolute;left:0;right:0;top:34px;height:3px;background:var(--orange)}
.nav a:first-child{margin-right:-1px}
.hero-photo{left:493px;top:166px;width:423px;height:356px;
  background:radial-gradient(ellipse at 60% 45%,#5a5540 0%,#2d2a1f 40%,#000 75%)}
.hero-title{left:185px;top:246px;color:var(--orange);font-weight:700;line-height:1}
.hero-title .l1{font-size:40px;display:block}
.hero-title .l2{font-size:49px;display:block;margin-top:2px}
.hero-copy{left:183px;top:343px;width:355px;font-size:11px;line-height:20.3px;color:#bdbdbd}
.btn-light{left:183px;top:436px;width:175px;height:36px;border-radius:3px;
  background:linear-gradient(#fff,#d8d8d8);color:#333;font-size:13px;text-align:center;line-height:36px}
.arrow-circle{width:46px;height:46px;border-radius:50%;background:var(--orange)}

/* section */
.section-title{left:0;width:1057px;top:540px;text-align:center;font-size:26px;font-weight:700;color:var(--orange);text-shadow:0 2px 3px #000}
.card{top:584px;width:263px;height:196px;border:6px solid var(--card-border);background:rgba(30,30,30,.55)}
.card h3{position:absolute;top:28px;left:0;right:0;text-align:center;font-size:13.5px;font-weight:700;color:#fff}
.card .product{position:absolute;left:14px;top:59px;width:76px;height:97px;border-radius:6px}
.card p{position:absolute;left:101px;top:72px;width:140px;font-size:8.5px;line-height:13.2px;color:#ddd;text-align:justify}
.btn{top:793px;width:127px;height:26px;background:var(--orange);color:#fff;font-size:10.5px;font-weight:700;display:flex;align-items:center;justify-content:center;gap:9px;text-transform:uppercase}

/* footer */
.footer{left:0;top:863px;width:1057px;height:337px;background:#000}
.foot-head{top:886px;font-size:14px;color:var(--orange);text-transform:uppercase}
.foot-list{top:931px;list-style:none;font-size:11px;line-height:21.1px;color:#e6e6e6}
.newsletter{left:677px;top:926px;width:245px;height:96px;background:#1b1b1b;border:1px solid #2a2a2a}
.newsletter h4{position:absolute;left:69px;top:6px;font-size:18px;font-weight:400;color:#8a8a8a}
.newsletter p{position:absolute;left:69px;top:31px;width:170px;font-size:8px;line-height:13px;color:#ddd}
.newsletter .field{position:absolute;left:16px;top:68px;width:186px;height:17px;background:#fff;border:1px solid #999;border-radius:2px}
.newsletter .go{position:absolute;left:210px;top:69px;width:17px;height:17px;border-radius:50%;background:#555;color:#fff;font-size:7.5px;font-weight:700;text-align:center;line-height:17px}
.social{left:680px;top:1077px;display:flex;gap:3px}
.social span{width:29px;height:29px;border-radius:50%;background:#fff;display:block}
.copyright{left:0;width:1057px;top:1157px;text-align:center;font-size:9.5px;color:#ddd}
</style>
</head>
<body>

<div class="abs search">Type search
  <svg width="10" height="10" viewBox="0 0 10 10"><circle cx="4" cy="4" r="3" fill="none" stroke="#888" stroke-width="1.4"/><line x1="6.2" y1="6.2" x2="9" y2="9" stroke="#888" stroke-width="1.6"/></svg>
</div>
<div class="abs util">
  <a href="#">My Account</a><span class="sep">|</span>
  <svg width="14" height="11" viewBox="0 0 14 11"><path d="M0 1h3l2 6h7l2-5H4" fill="none" stroke="#e9a21f" stroke-width="1.3"/><circle cx="6" cy="9.5" r="1.2" fill="#e9a21f"/><circle cx="11" cy="9.5" r="1.2" fill="#e9a21f"/></svg>
  <a href="#">(0 items )in my bag</a><span class="sep">|</span>
  <a href="#">My Wishlist</a><span class="sep">|</span>
  <a href="#">Checkout</a>
</div>
<a class="abs login" href="#">LOGIN</a>

<div class="abs panel"></div>
<div class="abs header-rule"></div>
<div class="abs brand"><span class="brand-mark"></span><span class="brand-name">QM Field Outfitters</span></div>
<nav class="abs nav">
  <a class="current" href="#">HOME</a>
  <a href="#">ABOUT</a>
  <a href="#">CUSTOMER SERVICE</a>
  <a href="#">SITE MAP</a>
  <a href="#">CONTACTS</a>
</nav>

<div class="abs hero-photo" role="img" aria-label="Special forces operator in helmet and goggles aiming a rifle"></div>
<h1 class="abs hero-title"><span class="l1">AUTOMATIC</span><span class="l2">WEAPONS</span></h1>
<p class="abs hero-copy">Lorem ipsum dolor sit amet, consectetur adipisicing elit, sed do eiusmod tempor incididunt ut labore et dolore magna aliqua. Ut enim ad minim veniam, quis nostrud exercitation ullamco laboris nisi ut aliquip ex ea commodo consequat.</p>
<a class="abs btn-light" href="#">VIEW COLLECTIONS</a>
<div class="abs arrow-circle" style="left:126px;top:297px"><svg width="46" height="46"><path d="M27 13 L18 23 L27 33" fill="none" stroke="#000" stroke-width="3"/></svg></div>
<div class="abs arrow-circle" style="left:897px;top:297px"><svg width="46" height="46"><path d="M19 13 L28 23 L19 33" fill="none" stroke="#000" stroke-width="3"/></svg></div>

<h2 class="abs section-title">WHAT WE SELL</h2>
<svg class="abs" style="left:115px;top:543px" width="18" height="28"><path d="M17 0 L0 14 L17 28Z" fill="#e9a21f"/></svg>
<svg class="abs" style="left:926px;top:543px" width="18" height="28"><path d="M0 0 L17 14 L0 28Z" fill="#e9a21f"/></svg>

<div class="abs card" style="left:115px">
  <h3>BULLETPROOF VEST</h3>
  <div class="product" role="img" aria-label="Camouflage bulletproof vest" style="background:linear-gradient(#3f5a45,#243528)"></div>
  <p>Lorem ipsum dolor sit amet, consectetur adipisicing elit, sed do eiusmod tempor incididunt ut labore et dolore magna aliqua. Ut enim ad minim veniam.</p>
</div>
<div class="abs card" style="left:398px">
  <h3>PROTECTIVE ARMOR PLATES</h3>
  <div class="product" role="img" aria-label="Tan plate carrier with black armor plate" style="background:linear-gradient(#6b5a35,#1c1c1c)"></div>
  <p>Lorem ipsum dolor sit amet, consectetur adipisicing elit, sed do eiusmod tempor incididunt ut labore et dolore magna aliqua. Ut enim ad minim veniam.</p>
</div>
<div class="abs card" style="left:678px">
  <h3>BALLISTIC HELMETS</h3>
  <div class="product" role="img" aria-label="Camouflage ballistic helmet" style="background:radial-gradient(circle,#8a877a,#3a3934)"></div>
  <p>Lorem ipsum dolor sit amet, consectetur adipisicing elit, sed do eiusmod tempor incididunt ut labore et dolore magna aliqua. Ut enim ad minim veniam.</p>
</div>

<a class="abs btn" href="#" style="left:114px">View More</a>
<a class="abs btn" href="#" style="left:249px"><svg width="16" height="12" viewBox="0 0 14 11"><path d="M0 1h3l2 6h7l2-5H4" fill="none" stroke="#fff" stroke-width="1.3"/><circle cx="6" cy="9.5" r="1.2" fill="#fff"/><circle cx="11" cy="9.5" r="1.2" fill="#fff"/></svg>Add to Cart</a>
<a class="abs btn" href="#" style="left:398px">View More</a>
<a class="abs btn" href="#" style="left:533px"><svg width="16" height="12" viewBox="0 0 14 11"><path d="M0 1h3l2 6h7l2-5H4" fill="none" stroke="#fff" stroke-width="1.3"/><circle cx="6" cy="9.5" r="1.2" fill="#fff"/><circle cx="11" cy="9.5" r="1.2" fill="#fff"/></svg>Add to Cart</a>
<a class="abs btn" href="#" style="left:678px">View More</a>
<a class="abs btn" href="#" style="left:814px"><svg width="16" height="12" viewBox="0 0 14 11"><path d="M0 1h3l2 6h7l2-5H4" fill="none" stroke="#fff" stroke-width="1.3"/><circle cx="6" cy="9.5" r="1.2" fill="#fff"/><circle cx="11" cy="9.5" r="1.2" fill="#fff"/></svg>Add to Cart</a>

<footer class="abs footer"></footer>
<h4 class="abs foot-head" style="left:115px">Information</h4>
<h4 class="abs foot-head" style="left:327px">Why Buy From Us</h4>
<h4 class="abs foot-head" style="left:538px">My Account</h4>
<h4 class="abs foot-head" style="left:677px">Newsletter Sign Up</h4>
<ul class="abs foot-list" style="left:115px">
  <li>About Us</li><li>Customer Service</li><li>Privacy Policy</li><li>Site Map</li><li>Search Terms</li><li>Advanced Search</li><li>Orders and Returns</li><li>Contact Us</li><li>Request RMA</li>
</ul>
<ul class="abs foot-list" style="left:327px">
  <li>Shipping &amp; Returns</li><li>Secure Shopping</li><li>International Shipping</li><li>Affiliates</li><li>Group Sales</li>
</ul>
<ul class="abs foot-list" style="left:538px">
  <li>Sign In</li><li>View Cart</li><li>My Wishlist</li><li>Track My Order</li><li>Help</li>
</ul>
<div class="abs newsletter">
  <svg style="position:absolute;left:18px;top:14px" width="40" height="40" viewBox="0 0 40 40">
    <path d="M4 14 L20 3 L36 14 V34 H4Z" fill="#cfcfcf" stroke="#555"/>
    <path d="M4 14 L20 25 L36 14" fill="none" stroke="#555"/>
    <circle cx="8" cy="32" r="7" fill="#444" stroke="#ccc"/>
    <path d="M5 32 L7.5 34.5 L11.5 29.5" fill="none" stroke="#fff" stroke-width="1.5"/>
  </svg>
  <h4>Subscribe</h4>
  <p>Lorem Ipsum is simply dummy text of the printing and typesetting industry.</p>
  <div class="field"></div>
  <div class="go">Go</div>
</div>
<h4 class="abs foot-head" style="left:679px;top:1044px">Connect With Us</h4>
<div class="abs social"><span></span><span></span><span></span><span></span></div>
<p class="abs copyright">© &nbsp;2013 QM FIELD OUTFITTERS,ALL RIGHTS RESERVED</p>

</body>
</html>
```